ご提案有難うございました。
最もサイトのトンマナにあっており、かつキャンペーンの売りが目立っていると感じたため、こちらのデザインを採用させて頂きました。
どれも素晴らしいご提案で御座いました。
また機会があればどうぞ宜しくお願い致します。
居酒屋予約 バナーデザイン バナー作成の仕事の依頼
希望する色 特になし・その他
バナーサイズ
• 300x250
目的・概要
居酒屋の割引キャンペーンページに誘導するために使用するバナー制作です。
依頼詳細
以下のページ等に設置致します。
https://www.pelmora-go.com/asia/japan/japa-japan/japa-restaurant/shinjuku-izakaya/
▽入れてほしい画像▽
会社ロゴ
▽入れてほしい文言▽
※以下の文章例を参考に、バナーデザインに映えるようご調整ください
■文章例
【最大100%割引】税込み2,160円以上の飲食で2,000円のキャッシュバックキャンペーン中!
【最大100%割引】居酒屋利用で2,000円のキャッシュバックキャンペーン中!
【最大100%割引】2,160円(税込)以上の居酒屋利用で2,000円の現金還元中!
Pelmora限定!居酒屋の利用で現金2,000円が貰える!
【最大100%割引】税込み2,160円の居酒屋利用で2,000円現金還元中!
Pelmora限定企画!税込み2,160円の居酒屋利用で2,000円現金還元中!!
3000店舗以上から選べる!税込み2,160円の居酒屋利用で2,000円現金還元中!!
居酒屋代金、実質最大100%オフ
3000店以上の居酒屋が実質最大100%割引
居酒屋の利用で漏れなく現金2,000円が貰える
▽バナーサイズ▽
▽納品形式▽
png/jpg
▽注意点・禁止事項▽
※他のクライアントへ既に提案した内容の転用など
※作成いただいたバナーに関して、納品後はクライアントに帰属します。
たくさんのウェブデザイナーの方からのご提案をお待ちしております!

```html
<!DOCTYPE html>
<html lang="ja">
<head>
<meta charset="utf-8">
<title>Pelmora 居酒屋キャッシュバック バナー</title>
<link rel="stylesheet" href="https://fonts.googleapis.com/css2?family=Noto+Sans+JP:wght@700;900&display=swap">
<style>
  :root {
    --brand-blue: #1e8fdc;
    --panel-blue: #2a9de6;
    --navy: #16366b;
    --cream: #fff4c4;
    --white: #ffffff;
    --beer-light: #f7d98a;
    --beer-deep: #d98d1c;
  }
  html, body {
    margin: 0;
    padding: 0;
    width: 1200px;
    height: 1000px;
    overflow: hidden;
    background: var(--white);
  }
  .banner {
    position: relative;
    width: 1200px;
    height: 1000px;
    overflow: hidden;
    font-family: "Noto Sans JP", sans-serif;
    background: var(--panel-blue);
  }
  .beer-photo {
    position: absolute;
    left: 0; top: 0;
    width: 1200px; height: 511px;
    background: radial-gradient(ellipse at 50% 45%, var(--beer-light) 0%, #eab54a 50%, var(--beer-deep) 100%);
    z-index: 1;
  }
  .brand-tab {
    position: absolute;
    left: 0; top: 0;
    width: 640px; height: 100px;
    background: var(--white);
    display: flex;
    align-items: center;
    padding-left: 34px;
    box-sizing: border-box;
    z-index: 3;
  }
  .brand-dot {
    width: 56px; height: 56px;
    border-radius: 50%;
    background: var(--brand-blue);
    margin-right: 18px;
  }
  .brand-name {
    font-weight: 900;
    font-size: 60px;
    color: var(--brand-blue);
    letter-spacing: 1px;
  }
  .offer-panel {
    position: absolute;
    left: 0; top: 511px;
    width: 1200px; height: 489px;
    background: var(--panel-blue);
    z-index: 2;
  }
  .max-tag {
    position: absolute;
    left: 49px; top: 507px;
    width: 54px; height: 171px;
    background: var(--navy);
    color: var(--white);
    font-weight: 900;
    font-size: 50px;
    line-height: 54px;
    writing-mode: vertical-rl;
    display: flex;
    align-items: center;
    justify-content: center;
    z-index: 4;
  }
  .headline-number {
    position: absolute;
    left: 118px; top: 311px;
    margin: 0;
    font-weight: 900;
    font-size: 400px;
    line-height: 1;
    letter-spacing: -8px;
    color: var(--cream);
    -webkit-text-stroke: 14px var(--navy);
    paint-order: stroke fill;
    transform: scaleX(0.82);
    transform-origin: left top;
    z-index: 4;
  }
  .headline-unit {
    position: absolute;
    left: 712px; top: 548px;
    margin: 0;
    font-weight: 900;
    font-size: 112px;
    line-height: 1.1;
    color: var(--navy);
    white-space: nowrap;
    z-index: 4;
  }
  .headline-unit .percent { font-size: 96px; margin-right: 8px; }
  .condition, .cashback {
    position: absolute;
    left: 0; width: 1200px;
    margin: 0;
    text-align: center;
    font-weight: 900;
    color: var(--white);
    -webkit-text-stroke: 8px var(--navy);
    paint-order: stroke fill;
    white-space: nowrap;
    z-index: 4;
  }
  .condition { top: 706px; font-size: 80px; line-height: 1.15; letter-spacing: -1px; }
  .cashback { top: 806px; font-size: 88px; line-height: 1.15; letter-spacing: -1px; }
  .small { font-size: 0.72em; }
</style>
</head>
<body>
<div class="banner">
  <div class="beer-photo" role="img" aria-label="泡立つジョッキの生ビールが並ぶ写真"></div>

  <header class="brand-tab">
    <span class="brand-dot"></span>
    <span class="brand-name">Pelmora</span>
  </header>

  <div class="offer-panel"></div>

  <div class="max-tag">最大</div>
  <p class="headline-number">100</p>
  <p class="headline-unit"><span class="percent">%</span>割引</p>

  <p class="condition">税込2,160<span class="small">円以上</span>居酒屋利用で</p>
  <p class="cashback">2,000<span class="small">円</span>キャッシュバック!</p>
</div>
</body>
</html>
```